Vardel paint banner

Banner same size Lumora Solutions advert banner
of previous one Lumora Solutions advert banner 215cm x 1055cm
but for a paint company, called Vardel Paint.
I want the concept to be similar to the attached, i want to put some real drum paint in front of the banner concept to look in Harmony with your concept on the banner.
The company is specialized in producing and painting houses and offices indoor and outdoor and applying epoxy on floors..

```html
<!DOCTYPE html>
<html lang="en">
<head>
<meta charset="utf-8">
<title>Vardel Paint Banner</title>
<link href="https://fonts.googleapis.com/css2?family=Anton&family=Poppins:ital,wght@0,600;0,700;1,600&display=swap" rel="stylesheet">
<style>
  :root {
    --backdrop: #1d1d1d;
    --banner-bg: #f7f6f9;
    --headline-red: #c4161c;
    --ink: #111111;
    --brand-blue: #2a6db5;
    --purple: #7446a8;
    --purple-deep: #5a2f8c;
    --white: #ffffff;
  }
  * { margin: 0; padding: 0; box-sizing: border-box; }
  html, body {
    width: 1200px; height: 1000px; overflow: hidden;
    background: var(--backdrop);
  }
  .banner {
    position: absolute; left: 50px; top: 388px;
    width: 1100px; height: 223px;
    background: var(--banner-bg);
    overflow: hidden;
  }
  .powder-burst {
    position: absolute; left: 0; top: 0; width: 470px; height: 223px;
    background:
      radial-gradient(ellipse 120px 90px at 140px 110px, #e8417f 0%, rgba(232,65,127,0) 100%),
      radial-gradient(ellipse 110px 80px at 90px 170px, #2fb7d9 0%, rgba(47,183,217,0) 100%),
      radial-gradient(ellipse 90px 70px at 30px 90px, #f2c230 0%, rgba(242,194,48,0) 100%),
      radial-gradient(ellipse 160px 60px at 280px 90px, rgba(120,210,235,.7) 0%, rgba(120,210,235,0) 100%),
      radial-gradient(ellipse 180px 80px at 300px 190px, rgba(240,150,200,.6) 0%, rgba(240,150,200,0) 100%),
      linear-gradient(90deg, #b23a8a 0%, rgba(247,246,249,0) 100%);
  }
  .logo-tab {
    position: absolute; left: 0; top: 0; width: 200px; height: 66px;
    background: var(--white);
    border-bottom-right-radius: 16px;
    clip-path: polygon(0 0, 100% 0, 88% 100%, 0 100%);
    display: flex; align-items: center; gap: 10px; padding-left: 44px;
  }
  .logo-dot {
    width: 30px; height: 30px; border-radius: 50%; background: var(--brand-blue);
  }
  .logo-name {
    font-family: 'Poppins', sans-serif; font-weight: 600; font-size: 18px;
    line-height: 19px; color: var(--brand-blue); text-align: center;
  }
  .headline {
    position: absolute; left: 200px; width: 700px; text-align: center;
    font-family: 'Anton', sans-serif; color: var(--headline-red);
    transform: skewX(-10deg);
    -webkit-text-stroke: 0; 
    text-shadow:
      2px 0 0 #fff, -2px 0 0 #fff, 0 2px 0 #fff, 0 -2px 0 #fff,
      2px 2px 0 #fff, -2px -2px 0 #fff, 2px -2px 0 #fff, -2px 2px 0 #fff,
      4px 4px 5px rgba(0,0,0,.45);
    letter-spacing: 0.5px;
  }
  .headline-top { top: 30px; font-size: 47px; line-height: 56px; }
  .headline-bottom { top: 88px; font-size: 56px; line-height: 64px; }
  .lead {
    position: absolute; left: 200px; width: 700px; text-align: center;
    font-family: 'Poppins', sans-serif; color: var(--ink);
  }
  .lead-main { top: 160px; font-size: 17px; font-weight: 600; }
  .lead-sub { top: 186px; font-size: 12px; font-weight: 600; }
  .paint-splash {
    position: absolute; left: 840px; top: 0; width: 260px; height: 223px;
    background: radial-gradient(ellipse 120px 105px at 140px 110px, var(--purple) 0%, var(--purple) 60%, rgba(116,70,168,0) 100%);
  }
  .vision-badge {
    position: absolute; left: 911px; top: 40px; width: 124px; height: 124px;
    border-radius: 50%; background: var(--white);
    box-shadow: 0 3px 6px rgba(0,0,0,.35);
    display: flex; align-items: center; justify-content: center;
  }
  .vision-badge-core {
    width: 108px; height: 108px; border-radius: 50%;
    background: var(--purple);
    display: flex; align-items: center; justify-content: center; text-align: center;
    font-family: 'Poppins', sans-serif; font-style: italic; font-weight: 600;
    font-size: 11.5px; line-height: 14px; color: var(--white);
    padding-bottom: 22px;
  }
  .vision-ribbon {
    position: absolute; left: 935px; top: 140px; width: 76px; height: 60px;
    background: linear-gradient(90deg, var(--purple-deep), var(--purple) 50%, var(--purple-deep));
  }
</style>
</head>
<body>
  <section class="banner">
    <div class="powder-burst" role="img" aria-label="Explosion of coloured paint powder in pink, blue, yellow and purple"></div>
    <div class="logo-tab">
      <span class="logo-dot"></span>
      <span class="logo-name">VARDEL<br>PAINT</span>
    </div>
    <h1 class="headline headline-top">LOOKING TO GIVE YOUR WALLS</h1>
    <p class="headline headline-bottom">NEW LIFE?</p>
    <p class="lead lead-main">Look no further than Vardel Paint,</p>
    <p class="lead lead-sub">Our high-quality paints come in a variety of vibrant colors and finishes,</p>
    <div class="paint-splash" role="img" aria-label="Purple paint splash with drips"></div>
    <div class="vision-ribbon"></div>
    <div class="vision-badge">
      <div class="vision-badge-core">Perfect for<br>bringing<br>your vision<br>to life.</div>
    </div>
  </section>
</body>
</html>
```